3 Simple Banners for Travel Company

We need 3 banners created:

728x90
468x60

160x600
120x600

300x250
250x250

There maybe 6 banners above but all we need is 3 designs and then to make that design fit the other banner. E.g. 728 banner is shrank to fit into a 468, BUT use the same design. This is required for 3 banner designs.

These must NOT be flash, only .gif and very professional looking.

please review our website to see and know the look and feel we are looking for: www.crewvoyago.eu
Updates

sorry guys the banner is meant to be 300x250 NOT 250x300

Thanks

Hi there,

We also have another project open if any of you are interested

http://tasks.pixelbazaar.example/task.aspx?id=51892

Thanks

Target Market(s)

travel industry employees (pilots, cabin crew, cruise ship staff, hotel staff etc...)

Industry/Entity Type

It Company

Requirements
Must have
• company logo

company mascots (kip & marla)

fb and twitter logo

Must inc the following words:

Interline Rates & Travel Discounts
Travel Industry Employees
Sign Up for FREE

```html
<!DOCTYPE html>
<html lang="en">
<head>
<meta charset="utf-8">
<title>CrewVoyago.eu banner set</title>
<link rel="stylesheet" href="https://fonts.googleapis.com/css2?family=Yanone+Kaffeesatz:wght@400;600&display=swap">
<style>
  :root {
    --page: #ffffff;
    --navy: #272a46;
    --navy-deep: #1b1d33;
    --skyline: #121322;
    --swoosh: #f2f2f6;
    --gold: #e6cc82;
    --gold-deep: #b58f3c;
    --silver: #e4e6ec;
    --silver-deep: #9a9eab;
    --button: #ffffff;
    --button-text: #1e2236;
    --arrow: #1b9be0;
    --pilot-tone: #3a3530;
    --crew-tone: #d8452a;
  }
  * { box-sizing: border-box; margin: 0; padding: 0; }
  html, body { width: 1200px; height: 732px; overflow: hidden; background: var(--page); }
  body { position: relative; font-family: "Yanone Kaffeesatz", "Arial Narrow", sans-serif; }

  .banner {
    position: absolute; overflow: hidden; border-radius: 8px;
    background: radial-gradient(ellipse at 50% 30%, #343858 0%, var(--navy) 55%, var(--navy-deep) 100%);
    box-shadow: 0 1px 3px rgba(0,0,0,.35);
  }
  .skyscraper { width: 160px; height: 600px; top: 57px; }
  .skyscraper--rates { left: 32px; }
  .skyscraper--staff { left: 220px; }
  .rectangle { width: 300px; height: 250px; top: 181px; }
  .rectangle--rates { left: 394px; }
  .rectangle--staff { left: 711px; }
  .leaderboard { width: 730px; height: 90px; left: 394px; }
  .leaderboard--rates { top: 449px; }
  .leaderboard--staff { top: 551px; }

  .skyline { position: absolute; left: 0; right: 0; bottom: 0; background: linear-gradient(var(--navy-deep), var(--skyline)); opacity: .85; }
  .swoosh { position: absolute; }
  .brand {
    position: absolute; color: var(--silver); font-weight: 600; line-height: .9;
    letter-spacing: .5px; text-align: center; white-space: nowrap; z-index: 2;
  }
  .headline { position: absolute; text-align: center; line-height: .92; text-transform: uppercase; white-space: nowrap; z-index: 2; }
  .headline span { display: block; }
  .gold { color: var(--gold); text-shadow: 0 1px 0 var(--gold-deep); }
  .silver { color: var(--silver); text-shadow: 0 1px 0 var(--silver-deep); }

  .mascot { position: absolute; z-index: 1; border-radius: 50% 50% 6px 6px / 35% 35% 6px 6px; }
  .mascot--pilot { background: linear-gradient(#2c2a2a 0%, #c99a6e 30%, #c99a6e 45%, var(--pilot-tone) 60%, #1c1c1e 100%); }
  .mascot--crew { background: linear-gradient(var(--crew-tone) 0%, #6b4028 25%, #6b4028 45%, var(--crew-tone) 60%, #a8321e 100%); }

  .signup {
    position: absolute; z-index: 3; display: flex; align-items: center; gap: 6px;
    background: var(--button); color: var(--button-text); border-radius: 3px;
    padding: 3px 8px 3px 4px; font-size: 18px; white-space: nowrap;
    box-shadow: 0 1px 2px rgba(0,0,0,.4);
  }
  .signup svg { flex: none; }
</style>
</head>
<body>

<!-- 160x600 : rates -->
<section class="banner skyscraper skyscraper--rates">
  <div class="brand" style="left:0;right:0;top:18px;font-size:40px;">Crew<br>Voyago.eu</div>
  <svg class="swoosh" style="left:0;top:95px" width="160" height="50" viewBox="0 0 160 50"><path d="M0 50 Q50 12 160 0 L160 8 Q60 18 0 50Z" fill="var(--swoosh)"/></svg>
  <div class="headline" style="left:0;right:0;top:150px;">
    <span class="gold" style="font-size:38px">Interline</span>
    <span class="gold" style="font-size:48px">Rates &amp;</span>
    <span class="silver" style="font-size:54px">Travel</span>
    <span class="silver" style="font-size:35px">Discounts</span>
  </div>
  <div class="skyline" style="height:140px"></div>
  <div class="mascot mascot--pilot" role="img" aria-label="Mascot Kip, cartoon airline captain in cap and uniform" style="left:10px;top:340px;width:140px;height:260px"></div>
  <div class="signup" style="left:15px;top:553px">
    <svg width="30" height="22" viewBox="0 0 30 22"><rect width="30" height="22" rx="2" fill="var(--arrow)"/><path d="M6 9h10V5l8 6-8 6v-4H6z" fill="#fff"/></svg>Sign Up for FREE
  </div>
</section>

<!-- 160x600 : staff -->
<section class="banner skyscraper skyscraper--staff">
  <div class="brand" style="left:0;right:0;top:18px;font-size:40px;">Crew<br>Voyago.eu</div>
  <svg class="swoosh" style="left:0;top:95px" width="160" height="50" viewBox="0 0 160 50"><path d="M0 50 Q50 12 160 0 L160 8 Q60 18 0 50Z" fill="var(--swoosh)"/></svg>
  <div class="headline" style="left:0;right:0;top:175px;">
    <span class="gold" style="font-size:56px">Travel</span>
    <span class="gold" style="font-size:42px">Industry</span>
    <span class="silver" style="font-size:35px">Employees</span>
  </div>
  <div class="skyline" style="height:150px"></div>
  <div class="mascot mascot--crew" role="img" aria-label="Mascot Marla, cartoon flight attendant in red uniform and hat" style="left:18px;top:330px;width:130px;height:270px"></div>
  <div class="signup" style="left:15px;top:553px">
    <svg width="30" height="22" viewBox="0 0 30 22"><rect width="30" height="22" rx="2" fill="var(--arrow)"/><path d="M6 9h10V5l8 6-8 6v-4H6z" fill="#fff"/></svg>Sign Up for FREE
  </div>
</section>

<!-- 300x250 : rates -->
<section class="banner rectangle rectangle--rates">
  <div class="brand" style="left:0;right:0;top:14px;font-size:40px;">CrewVoyago.eu</div>
  <svg class="swoosh" style="left:0;top:58px" width="300" height="46" viewBox="0 0 300 46"><path d="M0 46 Q90 8 300 0 L300 8 Q110 16 0 46Z" fill="var(--swoosh)"/></svg>
  <div class="skyline" style="height:95px"></div>
  <div class="mascot mascot--pilot" role="img" aria-label="Mascot Kip, cartoon airline captain in cap and uniform" style="left:4px;top:68px;width:96px;height:182px"></div>
  <div class="headline" style="left:104px;right:8px;top:104px;">
    <span class="gold" style="font-size:30px">Interline Rates &amp;</span>
    <span class="silver" style="font-size:30px">Travel Discounts</span>
  </div>
  <div class="signup" style="left:141px;top:206px">
    <svg width="30" height="22" viewBox="0 0 30 22"><rect width="30" height="22" rx="2" fill="var(--arrow)"/><path d="M6 9h10V5l8 6-8 6v-4H6z" fill="#fff"/></svg>Sign Up for FREE
  </div>
</section>

<!-- 300x250 : staff -->
<section class="banner rectangle rectangle--staff">
  <div class="brand" style="left:0;right:0;top:14px;font-size:40px;">CrewVoyago.eu</div>
  <svg class="swoosh" style="left:0;top:58px" width="300" height="46" viewBox="0 0 300 46"><path d="M0 46 Q90 8 300 0 L300 8 Q110 16 0 46Z" fill="var(--swoosh)"/></svg>
  <div class="skyline" style="height:95px"></div>
  <div class="mascot mascot--crew" role="img" aria-label="Mascot Marla, cartoon flight attendant in red uniform and hat" style="left:12px;top:62px;width:100px;height:188px"></div>
  <div class="headline" style="left:116px;right:8px;top:98px;">
    <span class="gold" style="font-size:32px">Travel Industry</span>
    <span class="silver" style="font-size:44px">Employees</span>
  </div>
  <div class="signup" style="left:141px;top:206px">
    <svg width="30" height="22" viewBox="0 0 30 22"><rect width="30" height="22" rx="2" fill="var(--arrow)"/><path d="M6 9h10V5l8 6-8 6v-4H6z" fill="#fff"/></svg>Sign Up for FREE
  </div>
</section>

<!-- 728x90 : rates -->
<section class="banner leaderboard leaderboard--rates">
  <div class="brand" style="left:18px;top:26px;font-size:40px;">CrewVoyago.eu</div>
  <svg class="swoosh" style="left:170px;top:0" width="110" height="90" viewBox="0 0 110 90"><path d="M0 90 Q40 20 110 0 L100 0 Q30 30 0 90Z" fill="var(--swoosh)"/></svg>
  <div class="skyline" style="left:270px;height:34px"></div>
  <div class="headline" style="left:270px;width:220px;top:10px;">
    <span class="gold" style="font-size:34px">Interline Rates &amp;</span>
    <span class="silver" style="font-size:34px">Travel Discounts</span>
  </div>
  <div class="mascot mascot--pilot" role="img" aria-label="Mascot Kip, cartoon airline captain in cap and uniform" style="left:496px;top:2px;width:80px;height:88px"></div>
  <div class="signup" style="left:582px;top:28px">
    <svg width="30" height="22" viewBox="0 0 30 22"><rect width="30" height="22" rx="2" fill="var(--arrow)"/><path d="M6 9h10V5l8 6-8 6v-4H6z" fill="#fff"/></svg>Sign Up for FREE
  </div>
</section>

<!-- 728x90 : staff -->
<section class="banner leaderboard leaderboard--staff">
  <div class="brand" style="left:18px;top:26px;font-size:40px;">CrewVoyago.eu</div>
  <svg class="swoosh" style="left:170px;top:0" width="110" height="90" viewBox="0 0 110 90"><path d="M0 90 Q40 20 110 0 L100 0 Q30 30 0 90Z" fill="var(--swoosh)"/></svg>
  <div class="skyline" style="left:270px;height:34px"></div>
  <div class="headline" style="left:290px;width:200px;top:8px;">
    <span class="gold" style="font-size:30px">Travel Industry</span>
    <span class="silver" style="font-size:42px">Employees</span>
  </div>
  <div class="mascot mascot--crew" role="img" aria-label="Mascot Marla, cartoon flight attendant in red uniform and hat" style="left:505px;top:2px;width:66px;height:88px"></div>
  <div class="signup" style="left:582px;top:28px">
    <svg width="30" height="22" viewBox="0 0 30 22"><rect width="30" height="22" rx="2" fill="var(--arrow)"/><path d="M6 9h10V5l8 6-8 6v-4H6z" fill="#fff"/></svg>Sign Up for FREE
  </div>
</section>

</body>
</html>
```